ZEPHIRO needs a new business card!

ZEPHIRO is a group of gaming enthusiasts who are looking for a new corporate business card.

The typeface should be modern and minimalist with attention paid to spacing between the letters and the letters 'zephiro' look relative to each other.

Should clean, crisp and minimalist - looking serious overall but with slight tweaks to the letters to make them look playful...

Black on white is fine.

Details on the card should include:
-the word 'zephiro'
-a job title (use any, for e.g. founder)
-a name (e.g. Ned Falka)
-phone number
-email address

For inspiration: http://brisket.tumblevane-cdn.example/wp-content/uploads/2013/07/mela-1.jpg

Target Market(s)

Video gaming enthusiasts

Industry/Entity Type

Business

Requirements
Must have
• Black letter on white background.
The word "zephiro"
Nice to have
• Maybe use a conservative font like Gibraltar or Helvetica and tweaking each letter individually.

You can insert normal job titles under the "zephiro" typeface
Should not have
• Should not be cartoony or childish fonts. No colors.

```html
<!DOCTYPE html>
<html lang="en">
<head>
<meta charset="utf-8">
<title>ZEPHIRO Business Card</title>
<link rel="stylesheet" href="https://fonts.googleapis.com/css2?family=Inter:wght@200;300&display=swap">
<style>
  :root {
    --backdrop: #d9dbe0;
    --card: #f7f7f6;
    --ink: #1a1a1c;
    --ink-soft: #3a3a3d;
    --rule: #2a2a2c;
  }
  html, body {
    margin: 0;
    padding: 0;
    width: 1200px;
    height: 864px;
    overflow: hidden;
    background: var(--backdrop);
  }
  .stage {
    position: relative;
    width: 1200px;
    height: 864px;
  }
  .business-card {
    position: absolute;
    left: 180px;
    top: 192px;
    width: 840px;
    height: 480px;
    background: var(--card);
    box-shadow: 0 18px 40px rgba(40, 44, 56, 0.22);
    font-family: "Inter", "Helvetica Neue", Arial, sans-serif;
    color: var(--ink);
  }
  .wordmark {
    position: absolute;
    left: 44px;
    top: 58px;
    margin: 0;
    font-weight: 200;
    font-size: 64px;
    letter-spacing: 3px;
    line-height: 1;
    color: var(--ink);
  }
  .divider {
    position: absolute;
    left: 368px;
    top: 0;
    width: 1.5px;
    height: 372px;
    background: var(--rule);
  }
  .contact {
    position: absolute;
    left: 369px;
    right: 0;
    top: 132px;
    text-align: center;
    font-weight: 300;
    color: var(--ink-soft);
  }
  .contact__name {
    margin: 0;
    font-size: 30px;
    font-weight: 200;
    letter-spacing: -0.5px;
  }
  .contact__title {
    margin: 2px 0 0 40px;
    font-size: 20px;
  }
  .contact__phone,
  .contact__email {
    margin: 0;
    font-size: 24px;
    line-height: 1.25;
  }
  .contact__phone {
    margin-top: 30px;
  }
</style>
</head>
<body>
  <main class="stage">
    <section class="business-card">
      <h1 class="wordmark">ZEPHIRO</h1>
      <div class="divider"></div>
      <div class="contact">
        <p class="contact__name">Ned Falka</p>
        <p class="contact__title">founder</p>
        <p class="contact__phone">555.014.2290</p>
        <p class="contact__email">NedFalka@mailvane.example</p>
      </div>
    </section>
  </main>
</body>
</html>
```